Nature and Scenic Photographs Business Card Design

I require a simple business card using the illustration that I have provided

Industry/Entity Type

Business

Contact Information for Business Card

Lyle Harcourt
Mobile: 0437812056
Skype: lyle.dorian.harcourt

```html
<!DOCTYPE html>
<html lang="en">
<head>
<meta charset="UTF-8">
<title>Lyle Harcourt – Photographer Business Card</title>
<link rel="stylesheet" href="https://fonts.googleapis.com/css2?family=Almendra:ital,wght@0,400;1,400&display=swap">
<style>
  :root {
    --page-bg: #2b2b2b;
    --card-bg: #0b0b0b;
    --text-green: #86c27a;
    --canopy-light: #b9cf7c;
    --leaf-bright: #7fa04a;
    --moss: #5f8a2e;
    --forest-mid: #36522a;
    --forest-dark: #16240f;
    --forest-deep: #0d160a;
    --floor-brown: #5a4a30;
  }
  * { margin: 0; padding: 0; box-sizing: border-box; }
  html, body {
    width: 1200px;
    height: 1000px;
    overflow: hidden;
    background: var(--page-bg);
  }
  .business-card {
    position: absolute;
    left: 100px;
    top: 215px;
    width: 1000px;
    height: 570px;
    background: var(--card-bg);
    box-shadow: 0 14px 40px rgba(0,0,0,0.55);
    font-family: "Almendra", serif;
    color: var(--text-green);
  }
  .forest-photo {
    position: absolute;
    left: 22px;
    top: 22px;
    width: 956px;
    height: 375px;
    background:
      radial-gradient(ellipse 22% 30% at 40% 18%, var(--canopy-light) 0%, transparent 70%),
      radial-gradient(ellipse 18% 22% at 62% 10%, var(--canopy-light) 0%, transparent 70%),
      radial-gradient(ellipse 30% 30% at 58% 72%, var(--moss) 0%, transparent 75%),
      radial-gradient(ellipse 22% 25% at 88% 65%, var(--floor-brown) 0%, transparent 75%),
      radial-gradient(ellipse 16% 45% at 22% 55%, var(--forest-deep) 0%, transparent 75%),
      radial-gradient(ellipse 12% 40% at 80% 25%, var(--forest-dark) 0%, transparent 75%),
      radial-gradient(ellipse 28% 35% at 10% 30%, var(--leaf-bright) 0%, transparent 75%),
      linear-gradient(180deg, var(--forest-mid) 0%, var(--forest-dark) 100%);
  }
  .contact-details {
    position: absolute;
    right: 58px;
    top: 408px;
    font-size: 25px;
    line-height: 33px;
    font-style: italic;
  }
  .identity {
    position: absolute;
    left: 170px;
    top: 448px;
  }
  .identity-name {
    font-size: 54px;
    font-weight: 400;
    font-style: italic;
    line-height: 60px;
  }
  .identity-role {
    font-size: 32px;
    font-weight: 400;
    font-style: italic;
    margin-left: 56px;
    line-height: 36px;
  }
</style>
</head>
<body>
  <div class="business-card">
    <div class="forest-photo" role="img" aria-label="Photograph of a lush rainforest floor with mossy fallen branches, palms and tree trunks"></div>
    <div class="contact-details">
      <p>Mobile: 0437812056</p>
      <p>Email: lyle.dh4@mailbox.net</p>
      <p>Skype: lyle.dorian.harcourt</p>
    </div>
    <div class="identity">
      <h1 class="identity-name">Lyle Harcourt</h1>
      <p class="identity-role">Photographer</p>
    </div>
  </div>
</body>
</html>
```